Wexley Foot & Ankle Martinsburg Window Vinyl Cling

Hi,
I'm looking to get a window decal done, but need it professionally designed.
-must be 24" x 24"
-Quorum Font
-Include our logo, Podiatry, phone number and website
- The goal is to make this eye catching.
Thank you,
Dorian

```html
<!DOCTYPE html>
<html lang="en">
<head>
<meta charset="utf-8">
<title>Wexley Foot &amp; Ankle Martinsburg – Window Cling</title>
<link href="https://fonts.googleapis.com/css2?family=Sansita:wght@700;800&display=swap" rel="stylesheet">
<style>
  :root {
    --orange: #f27f4a;
    --orange-deep: #d9562a;
    --teal: #5bc2a7;
    --white: #ffffff;
    --page: #eef1f5;
  }
  html, body {
    margin: 0;
    padding: 0;
    width: 1200px;
    height: 1200px;
    overflow: hidden;
    background: var(--page);
  }
  .cling {
    position: relative;
    width: 1200px;
    height: 1200px;
    box-sizing: border-box;
    border: 19px solid var(--orange);
    background: var(--white);
    font-family: "Sansita", "Georgia", serif;
    overflow: hidden;
  }
  .brand-mark {
    position: absolute;
    left: 36px;
    top: 120px;
    display: flex;
    align-items: center;
    gap: 14px;
    color: var(--teal);
    font-weight: 800;
    font-size: 30px;
    line-height: 1;
    letter-spacing: 1px;
  }
  .brand-mark .dot {
    width: 54px;
    height: 54px;
    border-radius: 50%;
    background: var(--teal);
    flex: none;
  }
  .headline {
    position: absolute;
    right: 21px;
    top: 52px;
    margin: 0;
    text-align: right;
    font-weight: 800;
    color: var(--orange);
    text-transform: uppercase;
    line-height: 1;
  }
  .headline .line {
    display: block;
    font-size: 118px;
    letter-spacing: 1px;
    height: 108px;
  }
  .headline .city {
    display: block;
    color: var(--teal);
    font-size: 76px;
    letter-spacing: 2px;
    margin-top: 4px;
  }
  .divider {
    position: absolute;
    left: 371px;
    top: 380px;
    width: 456px;
    height: 3px;
    border-radius: 2px;
    background: var(--teal);
  }
  .service {
    position: absolute;
    left: 0;
    width: 1162px;
    top: 404px;
    margin: 0;
    text-align: center;
    font-weight: 800;
    font-size: 134px;
    letter-spacing: 2px;
    line-height: 1;
    color: var(--orange);
  }
  .specialty-box {
    position: absolute;
    left: 204px;
    top: 546px;
    width: 790px;
    height: 204px;
    background: var(--orange);
    border-radius: 42px 0 42px 0;
  }
  .specialty-box p {
    margin: 0;
    position: absolute;
    left: 90px;
    right: 0;
    top: 12px;
    text-align: center;
    color: var(--white);
    font-weight: 700;
    font-size: 84px;
    line-height: 84px;
    text-shadow: 5px 5px 0 var(--orange-deep);
  }
  .foot-icon {
    position: absolute;
    left: 6px;
    top: 88px;
    width: 128px;
    height: 116px;
    border-radius: 30px 30px 40px 18px;
    background: var(--teal);
    border: 6px solid var(--white);
    box-sizing: border-box;
  }
  .contact {
    position: absolute;
    left: 246px;
    margin: 0;
    display: flex;
    align-items: center;
    gap: 22px;
    color: var(--teal);
    font-weight: 800;
    font-size: 80px;
    line-height: 1;
  }
  .contact svg { width: 62px; height: 62px; flex: none; }
  .contact-phone { top: 866px; }
  .contact-web { top: 975px; }
  .vine {
    position: absolute;
  }
  .vine-left {
    left: -19px;
    top: 580px;
    width: 125px;
    height: 120px;
    background: radial-gradient(ellipse at 40% 60%, rgba(91,194,167,0.55), rgba(91,194,167,0) 70%);
  }
  .vine-right {
    right: -19px;
    bottom: -19px;
    width: 230px;
    height: 250px;
    background: radial-gradient(ellipse at 75% 65%, rgba(242,127,74,0.5), rgba(242,127,74,0) 70%);
  }
</style>
</head>
<body>
<main class="cling">
  <div class="vine vine-left" role="img" aria-label="Teal leafy vine sprig decoration"></div>
  <div class="vine vine-right" role="img" aria-label="Orange leafy branch decoration in the corner"></div>

  <div class="brand-mark"><span class="dot"></span><span>WEXLEY FOOT &amp; ANKLE</span></div>

  <h1 class="headline">
    <span class="line">Wexley</span>
    <span class="line">Foot &amp; Ankle</span>
    <span class="city">Martinsburg</span>
  </h1>

  <div class="divider"></div>

  <h2 class="service">PODIATRY</h2>

  <div class="specialty-box">
    <div class="foot-icon" role="img" aria-label="Teal foot and ankle icon"></div>
    <p>Foot &amp; Ankle<br>Physicians</p>
  </div>

  <p class="contact contact-phone">
    <svg viewBox="0 0 64 64" aria-hidden="true">
      <path fill="#f27f4a" d="M14 6c3-2 6-1 8 2l6 9c1 2 1 5-1 7l-4 3c3 7 9 13 16 16l3-4c2-2 5-2 7-1l9 6c3 2 4 5 2 8l-3 4c-3 3-7 4-11 3C29 54 10 35 6 18c-1-4 0-8 3-11z"/>
      <path fill="none" stroke="#f27f4a" stroke-width="4" stroke-linecap="round" d="M38 8a20 20 0 0 1 18 18M37 17a11 11 0 0 1 10 10"/>
    </svg>
    (877) 555-0148
  </p>

  <p class="contact contact-web">
    <svg viewBox="0 0 64 64" aria-hidden="true">
      <circle cx="32" cy="32" r="29" fill="#f27f4a"/>
      <g fill="none" stroke="#ffffff" stroke-width="4">
        <ellipse cx="32" cy="32" rx="12" ry="29"/>
        <line x1="32" y1="3" x2="32" y2="61"/>
        <line x1="4" y1="22" x2="60" y2="22"/>
        <line x1="4" y1="42" x2="60" y2="42"/>
      </g>
    </svg>
    WexleyFeet.com
  </p>
</main>
</body>
</html>
```